Help me create an amazing cover for my first ebook!!

I am looking to have a modern and professional looking cover for my first ebook. It will be published through Borvex Quill Self Press and will need to follow their formatting and guidelines. I want the cover to have a modern and vibrant feel, that appeals to a millennial audience. This is a real estate book that is focused on a niche category catered to young professionals, so the idea would be to appeal to them.

Title:
The Twentysomething Playbook for Duplex Living

A Smart Property Buying Plan to Start Early, Cut Your Housing Costs (Sometimes to Zero), and Speed Up Your Path to Lasting Wealth.

Davin Osterlund

Target Market(s)

Real Estate investors, investors, millennials, young professionals, college educated, 20-40 years old.Financial freedom, finance.

Industry/Entity Type

Real Estate

Font styles to use
Sans Serif

Colors

Designer to choose colors to be used in the design.

Requirements
Must have
• Must follow the borvex quill self press format. I attached a screenshot of the details, it can also be found here: https://qsp.borvexbooks.example/en_US/help/topic/R481736025
• Must include this title:
• The Twentysomething Playbook for Duplex Living
• A Smart Property Buying Plan to Start Early, Cut Your Housing Costs (Sometimes to Zero), and Speed Up Your Path to Lasting Wealth.
• Davin Osterlund.
• I added examples of book covers I like to use as a guide, I also added some color pallette examples.
Nice to have
• Modern, clean design that's not too busy. Some sort of simple photo or illustration to incorporate in the cover along with the text would be nice.

```html
<!DOCTYPE html>
<html lang="en">
<head>
<meta charset="utf-8">
<title>The Twentysomething Playbook for Duplex Living — Ebook Cover</title>
<link href="https://fonts.googleapis.com/css2?family=Oswald:wght@500;600;700&family=Roboto+Condensed:ital,wght@0,400;1,700&display=swap" rel="stylesheet">
<style>
  :root {
    --page-bg: #ffffff;
    --navy: #141f47;
    --cyan: #22d3f5;
    --orange: #f6a524;
    --band: #0fbdf0;
    --ink: #152043;
    --sub-text: #e8ecf5;
  }
  html, body {
    margin: 0;
    padding: 0;
    width: 1200px;
    height: 1200px;
    overflow: hidden;
    background: var(--page-bg);
  }
  .canvas {
    position: relative;
    width: 1200px;
    height: 1200px;
  }
  .cover {
    position: absolute;
    left: 250px;
    top: 40px;
    width: 700px;
    height: 1120px;
    background: var(--navy);
    overflow: hidden;
  }
  .title { margin: 0; }
  .title-line {
    position: absolute;
    left: 0;
    width: 100%;
    margin: 0;
    text-align: center;
    font-family: "Oswald", sans-serif;
    font-weight: 600;
    color: var(--cyan);
    text-transform: uppercase;
    line-height: 1;
    white-space: nowrap;
  }
  .title-small { font-size: 64px; letter-spacing: -1px; }
  .title-top { top: 40px; }
  .title-mid { top: 132px; }
  .title-big { font-weight: 700; letter-spacing: -2px; }
  .title-duplex { top: 236px; font-size: 184px; }
  .title-living { top: 598px; font-size: 205px; }
  .scene-art {
    position: absolute;
    left: 0;
    top: 0;
    width: 700px;
    height: 1120px;
  }
  .subtitle {
    position: absolute;
    left: 30px;
    right: 30px;
    top: 832px;
    margin: 0;
    text-align: center;
    font-family: "Roboto Condensed", sans-serif;
    font-weight: 400;
    font-size: 26px;
    line-height: 37px;
    color: var(--sub-text);
  }
  .subtitle .accent {
    color: var(--orange);
    font-weight: 700;
    font-style: italic;
  }
  .author-band {
    position: absolute;
    left: 0;
    bottom: 0;
    width: 100%;
    height: 103px;
    background: var(--band);
    display: flex;
    align-items: center;
    justify-content: center;
  }
  .author-name {
    margin: 0;
    font-family: "Oswald", sans-serif;
    font-weight: 500;
    font-size: 48px;
    letter-spacing: 13px;
    padding-left: 13px;
    color: var(--ink);
    text-transform: uppercase;
    line-height: 1;
    white-space: nowrap;
  }
</style>
</head>
<body>
<main class="canvas">
  <article class="cover">
    <h1 class="title">
      <span class="title-line title-small title-top">The Twentysomething</span>
      <span class="title-line title-small title-mid">Playbook for</span>
      <span class="title-line title-big title-duplex">Duplex</span>
      <span class="title-line title-big title-living">Living</span>
    </h1>

    <svg class="scene-art" viewBox="0 0 700 1120">
      <rect x="160" y="462" width="290" height="140" rx="14" fill="#ffffff" fill-opacity="0.9"
            role="img" aria-label="White illustration of small houses, trees and an apartment block"/>
      <path d="M115 608 C 300 600, 500 560, 648 404" fill="none" stroke="var(--orange)" stroke-width="9" stroke-linecap="round"/>
      <path d="M612 404 L 656 394 L 652 440" fill="none" stroke="var(--orange)" stroke-width="9" stroke-linecap="round" stroke-linejoin="round"/>
    </svg>

    <p class="subtitle">
      A Smart Property Buying Plan<br>
      <span class="accent">to Start Early</span>, <span class="accent">Cut Your Housing Costs</span><br>
      (Sometimes to Zero), and <span class="accent">Speed Up Your Path</span><br>
      to Lasting Wealth.
    </p>

    <footer class="author-band">
      <p class="author-name">Davin Osterlund</p>
    </footer>
  </article>
</main>
</body>
</html>
```